Bright Path Flyer Design for Virtual Online Clinic. -5.5 x 8.5 inches (half sheet)

We need a clean, modern flyer design for Bright Path, a new virtual walk-in clinic based in British Columbia. The flyer will be used in libraries, pharmacies, and community centers to help residents easily access primary care through their Bright Path NFC access card.
The flyer will ask a question : NEED A DOCTOR? This should be large and attention grabbing.
The design should clearly feature a Bright Path card image (the access card) as the centerpiece and visually show how patients can use it to book appointments. The tone should feel trustworthy, healthcare-oriented, and community-friendly — clean fonts, clear spacing, and strong readability from a distance.

Side One: This card has the NFC Access Card.
NEED A DOCTOR? (Large Font, Attention Grabbing)
How to Book an Appointment using your Bright Path Card
Step 1: Tap Your Card on Your Phone
Hold your card near the back of your phone.
It will activate automatically — no app needed.
The Bright Path scheduler will open.
Step 2: Schedule Your Appointment
Select your clinical concern.
Choose your time window.
Register (only once).
Confirm your appointment.
Step 3: Relax, we’ll take care of the rest
A doctor will call during your scheduled time.
Once booked, you’ll be able to call our office.
No emails, no texts — just a real person.
It’s that simple.
Side Two:
About Bright Path
Created by Dr. Marcus Ferrigan
Bright Path was founded to make healthcare simple and convenient. Prescription renewals. Common infections. Medical notes. And so much more.
Our doctors can address 120+ health concerns virtually — providing quality care without the waiting room. No waiting rooms. Just real doctors providing real care.
Why Patients Choose Bright Path
Easy access – book and be seen from anywhere in BC.
Effortless booking – tap your Bright Path Card to begin.
Trusted physicians – every visit is with a licensed BC family doctor.
How It Works
Book your visit — choose a time window that fits your day.
Join the queue — you’ll be called when it’s your turn.
Speak directly with your doctor — simple, secure, and stress-free.
Convenient Care for Common Concerns

Additional Details.
Please find the domain to be launched soon. I've attached the NFC card file for review, it is 85.5 mm x 54 mm. The card will be glued to the flyer.
I've attached examples of flyers but they are not the look I am seeking and I am looking for creative solutions.
Thank you!
http://brightpath-example.test/

Adult Patients in British Columbia

Healthcare

• Looking for clean lines, uniform appearance, and high legibility i.e poppins

0054AA
0677BA
7BADD7
CADEEF
E8F1F8

• Need A Doctor?
• Elegant style, not too busy, clear layout.
• Clutter, look cheap - review examples.

```html
<!DOCTYPE html>
<html lang="en">
<head>
<meta charset="utf-8">
<title>Bright Path Flyer – Two Sides</title>
<link href="https://fonts.googleapis.com/css2?family=Anton&family=Oswald:wght@500;600;700&family=Roboto+Condensed:wght@400;500;700&family=Libre+Baskerville&display=swap" rel="stylesheet">
<style>
:root{
  --navy:#253a8a;
  --navy-dark:#1e2f78;
  --band:#3a51a6;
  --accent:#3657d6;
  --sky:#cadeef;
  --mist:#e8f1f8;
  --grey-bg:#cbcbcb;
  --grey-text:#7a7a7a;
  --ink:#222;
  --white:#fff;
}
*{box-sizing:border-box;margin:0;padding:0}
html,body{width:1200px;height:879px;overflow:hidden;background:var(--grey-bg);font-family:"Roboto Condensed",sans-serif;color:var(--ink)}
.canvas{position:relative;width:1200px;height:879px}
.page{position:absolute;top:112px;width:424px;height:656px;background:var(--white);overflow:hidden}
.page--front{left:160px}
.page--back{left:616px}
.abs{position:absolute}

/* ---------- front ---------- */
.hero-photo{left:0;top:0;width:424px;height:274px;background:linear-gradient(100deg,#b9c8d6 0%,#e3e8ee 45%,#d9cfc6 70%,#eef0f2 100%)}
.lower-band{left:0;top:274px;width:424px;height:172px;background:var(--navy)}
.logo-blob{left:0;top:0;width:128px;height:66px;background:var(--navy);border-bottom-right-radius:60px 50px}
.brand{font-family:"Roboto Condensed",sans-serif;font-weight:500;color:var(--white);display:flex;align-items:center;gap:5px;white-space:nowrap}
.brand__dot{width:7px;height:7px;border-radius:50%;background:currentColor}
.logo-blob .brand{position:absolute;left:16px;top:24px;font-size:16px}
.nfc-note{left:141px;top:10px;font-family:"Oswald",sans-serif;font-weight:500;font-size:11.5px;color:var(--navy)}
.oval-clip{left:0;top:0;width:424px;height:316px;overflow:hidden}
.headline-oval{position:absolute;left:21px;top:143px;width:374px;height:300px;border-radius:50%;background:var(--navy);border:4px solid var(--white)}
.access-card{left:149px;top:88px;width:127px;height:72px;background:var(--white);border:2px solid var(--white);box-shadow:0 1px 3px rgba(0,0,0,.25);display:flex}
.access-card__art{width:38px;height:100%;background:linear-gradient(160deg,#2b3f93,#1f2f78)}
.access-card__body{position:relative;flex:1}
.access-card .brand{color:var(--navy);font-size:11px;position:absolute;left:14px;top:27px}
.access-card__tap{position:absolute;right:6px;bottom:7px;font-size:4.5px;color:var(--navy)}
.access-card__nfc{position:absolute;right:5px;top:5px;width:6px;height:6px;background:var(--navy);border-radius:1px}
.headline{left:0;width:424px;text-align:center;font-family:"Anton",sans-serif;font-weight:400;color:var(--white);line-height:1;font-size:66px;letter-spacing:.5px}
.headline--one{top:192px}
.headline--two{top:263px}
.booking-title{left:0;top:329px;width:424px;text-align:center;font-family:"Oswald",sans-serif;font-weight:600;font-size:17px;line-height:20.5px;color:var(--white)}
.step-photo{top:375px;width:122px;height:122px;border-radius:50%;border:3px solid var(--white);box-shadow:0 0 0 1px rgba(0,0,0,.05)}
.step-photo--1{left:13px;background:radial-gradient(circle at 45% 40%,#d8dde2,#a9b3bd)}
.step-photo--2{left:152px;background:radial-gradient(circle at 50% 45%,#f1f1f1,#c4c9cf)}
.step-photo--3{left:289px;background:radial-gradient(circle at 50% 40%,#f4f4f4,#cfd3d8)}
.step-pill{top:505px;width:84px;height:15px;border-radius:8px;background:var(--navy);color:var(--white);font-family:"Oswald",sans-serif;font-weight:500;font-size:10px;line-height:15px;text-align:center}
.step-list{top:531px;list-style:none;font-size:8px;line-height:9.4px}
.step-list li{position:relative;padding-left:12px;margin-bottom:3.6px}
.step-list li::before{content:"";position:absolute;left:0;top:0.5px;width:8px;height:8px;border-radius:50%;background:var(--navy)}
.step-list li::after{content:"";position:absolute;left:2.6px;top:2.3px;width:2.4px;height:3.6px;border:solid var(--white);border-width:0 1.2px 1.2px 0;transform:rotate(45deg)}
.step-list--1{left:19px;width:113px}
.step-list--2{left:157px;width:120px}
.step-list--3{left:289px;width:122px}
.justify{text-align:justify}
.front-wave{left:0;top:608px;width:424px;height:48px}
.front-url{left:59px;top:625px;font-family:"Oswald",sans-serif;font-weight:600;font-size:16.5px;color:var(--white)}

/* ---------- back ---------- */
.about-panel{left:0;top:0;width:249px;height:367px;background:var(--navy);border-bottom-right-radius:46px}
.side-band{left:283px;top:51px;width:142px;height:275px;background:var(--navy)}
.photo-ring{left:207px;top:75px;width:228px;height:228px;border-radius:50%;border:2px solid var(--navy-dark);background:var(--white)}
.circle-photo{left:216px;top:84px;width:210px;height:210px;border-radius:50%;background:radial-gradient(circle at 60% 45%,#f3f4f6,#c9ced6 70%,#aab2bd)}
.about-title{left:19px;top:46px;display:flex;align-items:center;gap:8px;color:var(--white)}
.about-title__word{font-family:"Anton",sans-serif;font-size:26px;letter-spacing:.3px;line-height:1.1}
.about-title .brand{font-size:17px}
.created-by{left:18px;top:91px;font-family:"Libre Baskerville",serif;font-size:25px;color:var(--white)}
.name-band{left:0;top:123px;width:192px;height:38px;background:var(--band)}
.name-band__text{position:absolute;left:17px;top:9px;font-family:"Libre Baskerville",serif;font-size:16.5px;color:var(--white);white-space:nowrap}
.about-copy{left:19px;top:170px;width:173px;color:var(--white);font-size:9.4px;line-height:15px;text-align:justify}
.about-copy--two{top:235px;text-align:left;line-height:14.5px}
.big-claim{font-family:"Oswald",sans-serif;font-weight:500;font-size:14px}
.check-list{left:19px;top:301px;list-style:none;color:var(--white);font-size:12.5px}
.check-list li{position:relative;padding-left:18px;height:19.5px}
.check-list li::before{content:"";position:absolute;left:0;top:2px;width:11px;height:11px;border-radius:50%;border:1px solid var(--white)}
.check-list li::after{content:"";position:absolute;left:4px;top:4.3px;width:3px;height:5px;border:solid var(--white);border-width:0 1px 1px 0;transform:rotate(45deg)}
.why-title{left:38px;top:381px;font-family:"Anton",sans-serif;font-weight:400;font-size:19px;letter-spacing:.4px;color:var(--grey-text);white-space:nowrap}
.why-title span{color:var(--navy)}
.feature{display:flex;gap:10px}
.feature__icon{width:40px;height:45px;background:var(--navy);border-radius:3px 14px 3px 14px;outline:1px dotted var(--navy);outline-offset:2px;display:flex;align-items:center;justify-content:center}
.feature__title{font-family:"Oswald",sans-serif;font-weight:500;font-size:9.5px;color:var(--accent);margin-bottom:2px}
.feature__text{font-size:8.4px;line-height:10.3px;width:72px;text-align:justify}
.feature--1{left:19px;top:421px}
.feature--2{left:150px;top:421px}
.feature--3{left:283px;top:415px}
.works-band{left:0;top:479px;width:425px;height:125px;background:var(--navy)}
.works-title{left:27px;top:511px;font-family:"Anton",sans-serif;font-weight:400;font-size:22px;line-height:29px;color:var(--white)}
.works-rule{height:1px;background:var(--white)}
.step-num{top:497px;width:32px;height:32px;border-radius:50%;background:var(--white);border:2px solid var(--white);box-shadow:inset 0 0 0 1.5px var(--navy);color:var(--navy);font-family:"Anton",sans-serif;font-size:17px;line-height:28px;text-align:center}
.works-step{top:535px;width:86px;text-align:center;color:var(--white)}
.works-step__title{font-family:"Oswald",sans-serif;font-weight:500;font-size:9.3px;line-height:11.5px;margin-bottom:2px}
.works-step__text{font-size:8.3px;line-height:10.3px}
.care-pill{left:105px;top:589px;width:214px;height:23px;border-radius:12px;background:var(--accent);color:var(--white);font-family:"Oswald",sans-serif;font-weight:500;font-size:12px;line-height:23px;text-align:center}
.back-url{left:0;top:616px;width:425px;text-align:center;font-family:"Oswald",sans-serif;font-weight:600;font-size:20px;color:var(--navy)}
.dotted-rule{top:631px;height:0;border-top:1px dotted var(--navy)}
</style>
</head>
<body>
<main class="canvas">

  <!-- Side one -->
  <section class="page page--front">
    <div class="abs hero-photo" role="img" aria-label="Photo of a smiling female doctor in a white coat with a stethoscope, blurred clinic corridor behind"></div>
    <div class="abs lower-band"></div>
    <div class="abs logo-blob"><div class="brand"><span class="brand__dot"></span>Bright Path</div></div>
    <p class="abs nfc-note">This card has the NFC Access Card</p>
    <div class="abs oval-clip"><div class="headline-oval"></div></div>
    <div class="abs access-card">
      <div class="access-card__art" role="img" aria-label="Blue artwork panel of the access card"></div>
      <div class="access-card__body">
        <span class="access-card__nfc"></span>
        <div class="brand"><span class="brand__dot"></span>Bright Path</div>
        <span class="access-card__tap">Tap Here to Book</span>
      </div>
    </div>
    <h1 class="abs headline headline--one">NEED A</h1>
    <h1 class="abs headline headline--two">DOCTOR?</h1>
    <h2 class="abs booking-title">How to Book an Appointment using your<br>Bright Path Card</h2>

    <div class="abs step-photo step-photo--1" role="img" aria-label="Photo of a hand holding a phone near the access card"></div>
    <div class="abs step-photo step-photo--2" role="img" aria-label="Photo of clinic staff with headsets scheduling appointments"></div>
    <div class="abs step-photo step-photo--3" role="img" aria-label="Photo of a doctor on a phone call at a desk"></div>

    <div class="abs step-pill" style="left:32px">STEP 1</div>
    <div class="abs step-pill" style="left:171px">STEP 2</div>
    <div class="abs step-pill" style="left:308px">STEP 3</div>

    <ul class="abs step-list step-list--1">
      <li>Tap Your Card on Your Phone</li>
      <li class="justify">Hold your card near the back of your phone.</li>
      <li class="justify">It will activate automatically – no app needed.</li>
      <li class="justify">The Bright Path scheduler will open.</li>
    </ul>
    <ul class="abs step-list step-list--2">
      <li>Schedule Your Appointment</li>
      <li>Select your clinical concern.</li>
      <li>Choose your time window.</li>
      <li>Register (only once).</li>
      <li>Confirm your appointment.</li>
    </ul>
    <ul class="abs step-list step-list--3">
      <li>Relax, we’ll take care of the rest</li>
      <li class="justify">A doctor will call during your scheduled time.</li>
      <li class="justify">Once booked, you’ll be able to call our office.</li>
      <li class="justify">No emails, no texts – just a real person.</li>
      <li>It’s that simple.</li>
    </ul>

    <svg class="abs front-wave" viewBox="0 0 424 48" preserveAspectRatio="none" aria-hidden="true">
      <path d="M0 48 L0 36 C60 8 160 4 240 12 C320 20 380 16 424 6 L424 48 Z" fill="#3a51a6"/>
      <path d="M0 48 L0 44 C70 18 170 14 250 20 C330 26 385 20 424 12 L424 48 Z" fill="#253a8a"/>
    </svg>
    <p class="abs front-url">www.brightpath-example.test</p>
  </section>

  <!-- Side two -->
  <section class="page page--back">
    <div class="abs about-panel"></div>
    <div class="abs side-band"></div>
    <div class="abs photo-ring"></div>
    <div class="abs circle-photo" role="img" aria-label="Photo of a doctor's arms crossed holding a stethoscope"></div>

    <div class="abs about-title"><span class="about-title__word">About</span><span class="brand"><span class="brand__dot"></span>Bright Path</span></div>
    <p class="abs created-by">Created by</p>
    <div class="abs name-band"><span class="name-band__text">Dr. Marcus Ferrigan</span></div>

    <p class="abs about-copy">Bright Path was founded to make healthcare simple and convenient. Prescription renewals. Common infections. Medical notes. And so much more.</p>
    <p class="abs about-copy about-copy--two">Our doctors can address <span class="big-claim">120+ HEALTH CONCERNS</span> virtually – providing quality care without the waiting room.</p>

    <ul class="abs check-list">
      <li>No waiting rooms</li>
      <li>Just real doctors providing real care</li>
    </ul>

    <h3 class="abs why-title">WHY PATIENTS CHOOSE <span>BRIGHT PATH</span></h3>

    <div class="abs feature feature--1">
      <div class="feature__icon">
        <svg width="20" height="20" viewBox="0 0 20 20" aria-hidden="true"><circle cx="10" cy="10" r="7.5" fill="none" stroke="#fff" stroke-width="2"/><path d="M6.5 10.2l2.4 2.4 4.6-4.8" fill="none" stroke="#fff" stroke-width="2"/></svg>
      </div>
      <div><p class="feature__title">Easy Access</p><p class="feature__text">Book and be seen from anywhere in BC.</p></div>
    </div>
    <div class="abs feature feature--2">
      <div class="feature__icon">
        <svg width="16" height="22" viewBox="0 0 16 22" aria-hidden="true"><rect x="2" y="1" width="12" height="20" rx="2" fill="none" stroke="#fff" stroke-width="1.8"/><path d="M5 11l2.2 2.2 4-4.2" fill="none" stroke="#fff" stroke-width="1.8"/></svg>
      </div>
      <div><p class="feature__title">Effortless Booking</p><p class="feature__text">Tap your Bright Path Card to begin.</p></div>
    </div>
    <div class="abs feature feature--3">
      <div class="feature__icon">
        <svg width="20" height="20" viewBox="0 0 20 20" aria-hidden="true"><path d="M7.5 2h5v5.5H18v5h-5.5V18h-5v-5.5H2v-5h5.5z" fill="#fff"/></svg>
      </div>
      <div><p class="feature__title">Trusted Physicians</p><p class="feature__text" style="line-height:10.5px">Every visit is with a licensed BC family doctor.</p></div>
    </div>

    <div class="abs works-band"></div>
    <div class="abs works-rule" style="left:0;top:505px;width:84px"></div>
    <h3 class="abs works-title">HOW IT<br>WORKS</h3>
    <div class="abs works-rule" style="left:0;top:581px;width:84px"></div>

    <div class="abs step-num" style="left:145px">1</div>
    <div class="abs step-num" style="left:249px">2</div>
    <div class="abs step-num" style="left:352px">3</div>
    <svg class="abs" style="left:192px;top:503px" width="46" height="12" viewBox="0 0 46 12" aria-hidden="true"><path d="M2 10 C14 0 32 0 42 9" fill="none" stroke="#fff" stroke-width="1" stroke-dasharray="3 2"/><path d="M38 9l4 1 0-4" fill="none" stroke="#fff" stroke-width="1"/></svg>
    <svg class="abs" style="left:296px;top:503px" width="46" height="12" viewBox="0 0 46 12" aria-hidden="true"><path d="M2 10 C14 0 32 0 42 9" fill="none" stroke="#fff" stroke-width="1" stroke-dasharray="3 2"/><path d="M38 9l4 1 0-4" fill="none" stroke="#fff" stroke-width="1"/></svg>

    <div class="abs works-step" style="left:118px"><p class="works-step__title">Book Your Visit</p><p class="works-step__text">Choose a time window that fits your day.</p></div>
    <div class="abs works-step" style="left:222px"><p class="works-step__title">Join the Queue</p><p class="works-step__text">You’ll be called when it’s your turn.</p></div>
    <div class="abs works-step" style="left:325px"><p class="works-step__title">Speak directly with your doctor</p><p class="works-step__text">Simple, Secure, and Stress-free.</p></div>

    <div class="abs care-pill">Convenient Care for Common Concerns</div>
    <div class="abs dotted-rule" style="left:0;width:86px"></div>
    <p class="abs back-url">www.brightpath-example.test</p>
    <div class="abs dotted-rule" style="left:339px;width:86px"></div>
  </section>

</main>
</body>
</html>
```